Electrical company 7Kites needs a new logo design.

Need business cards for electrical company.
Modern/luxury/ Smart.
Thinking Black with White text.
Attached the logo below.

We would like two versions made - each one having different contact information on (one for each company directors). Both however will have same company address -

Fennel Court 31-35 Garwick Lane
Canvey Island
Essex Date
SS7 4PT

Contact details 1 -
Gareth Penwright
Director
gaz@7kites-demo.co.uk
07700900318

Contact details 2 -
Kieran Ashbury
Director
07700900742
kieran@7kites-demo.co.uk

Logo Text

7 Kites Electrical Solutions

```html
<!DOCTYPE html>
<html lang="en">
<head>
<meta charset="utf-8">
<title>7Kites Electrical Solutions – Business Card</title>
<link rel="stylesheet" href="https://fonts.googleapis.com/css2?family=Hind:wght@400;500;600&display=swap">
<style>
  :root {
    --page: #eceef2;
    --card-dark: #3a3a3b;
    --card-light: #ffffff;
    --card-light-end: #eeeff1;
    --ink: #2b2b2c;
    --ink-soft: #3d3d3f;
    --white: #ffffff;
    --pattern-dark: #141414;
    --pattern-mid: #6c6c6c;
  }
  * { box-sizing: border-box; margin: 0; padding: 0; }
  html, body { width: 1200px; height: 1200px; overflow: hidden; }
  body {
    background: var(--page);
    font-family: "Hind", sans-serif;
    position: relative;
  }
  .card {
    position: absolute;
    left: 221px;
    width: 750px;
    height: 450px;
    overflow: hidden;
    box-shadow: 0 6px 18px rgba(60, 70, 90, 0.18);
  }
  .card--front { top: 106px; background: var(--card-dark); }
  .card--back {
    top: 625px;
    background: linear-gradient(180deg, var(--card-light) 0%, var(--card-light-end) 100%);
  }

  .brand {
    position: absolute;
    font-family: "Hind", sans-serif;
    font-weight: 500;
    line-height: 1;
    white-space: nowrap;
    transform: translate(-50%, -50%);
  }
  .card--front .brand {
    color: var(--white);
    font-size: 46px;
    left: 50%;
    top: 198px;
  }
  .card--back .brand {
    color: var(--ink);
    font-size: 30px;
    left: 204px;
    top: 210px;
  }

  .pattern-band {
    position: absolute;
    left: 0; right: 0; bottom: 0;
    height: 85px;
    background: linear-gradient(90deg, var(--pattern-dark), var(--pattern-mid) 30%, var(--pattern-dark) 55%, var(--pattern-mid) 80%, var(--pattern-dark));
  }

  .divider {
    position: absolute;
    left: 378px;
    top: 100px;
    width: 2px;
    height: 260px;
    background: linear-gradient(180deg, rgba(0,0,0,0), rgba(0,0,0,0.07) 40%, rgba(0,0,0,0.07) 70%, rgba(0,0,0,0));
  }

  .contact {
    position: absolute;
    left: 426px;
    top: 168px;
    color: var(--ink);
  }
  .contact__name {
    font-size: 21px;
    font-weight: 400;
    letter-spacing: 0.02em;
    line-height: 1.1;
  }
  .contact__name strong { font-weight: 600; }
  .contact__role {
    font-size: 14px;
    color: var(--ink-soft);
    margin-top: 2px;
  }
  .contact__list {
    list-style: none;
    margin-top: 18px;
    font-size: 13.5px;
    font-weight: 500;
    line-height: 1.2;
  }
  .contact__item {
    display: flex;
    align-items: flex-start;
    gap: 7px;
    margin-bottom: 8px;
  }
  .contact__icon { width: 11px; height: 13px; flex: none; margin-top: 1px; fill: var(--ink); }

  .wave { position: absolute; left: 0; bottom: 0; width: 750px; height: 130px; }
</style>
</head>
<body>

  <section class="card card--front">
    <div class="brand">7Kites</div>
    <div class="pattern-band" role="img" aria-label="Band of grey and black faceted triangle pattern"></div>
  </section>

  <section class="card card--back">
    <div class="brand">7Kites</div>

    <div class="divider"></div>

    <div class="contact">
      <h1 class="contact__name">KIERAN <strong>ASHBURY</strong></h1>
      <p class="contact__role">DIRECTOR</p>
      <ul class="contact__list">
        <li class="contact__item">
          <svg class="contact__icon" viewBox="0 0 12 16"><path d="M6 0a6 6 0 0 0-6 6c0 4.5 6 10 6 10s6-5.5 6-10a6 6 0 0 0-6-6zm0 8.5A2.5 2.5 0 1 1 6 3.5a2.5 2.5 0 0 1 0 5z"/></svg>
          <span>Fennel Court 31-35 Garwick Lane,<br>Canvey Island, SS7 4PT</span>
        </li>
        <li class="contact__item">
          <svg class="contact__icon" viewBox="0 0 16 16"><path d="M3.6 0.6l2.2 2.8c.4.5.3 1.1-.1 1.5L4.6 6c.9 2 2.5 3.6 4.5 4.5l1.1-1.1c.4-.4 1-.5 1.5-.1l2.8 2.2c.5.4.6 1.1.1 1.6l-1.3 1.3C11.9 15.8 10 16 8 14.6 5 12.5 3.5 11 1.4 8 0 6 .2 4.1 1.6 2.6L2 2.2c.5-.5 1.2-.4 1.6.1z"/></svg>
          <span>07700900742</span>
        </li>
        <li class="contact__item">
          <svg class="contact__icon" viewBox="0 0 16 12"><path d="M0 0h16v12H0zM1.5 1.5L8 6.8l6.5-5.3v-.1h-13zm0 1.8v7.2h13V3.3L8 8.6z"/></svg>
          <span>kieran@7kites-demo.co.uk</span>
        </li>
      </ul>
    </div>

    <svg class="wave" viewBox="0 0 750 130" preserveAspectRatio="none" role="img" aria-label="Wave of grey and black faceted triangle pattern">
      <defs>
        <linearGradient id="wave-fill" x1="0" x2="1" y1="0" y2="0">
          <stop offset="0" stop-color="#1a1a1a"/>
          <stop offset="0.3" stop-color="#6a6a6a"/>
          <stop offset="0.55" stop-color="#161616"/>
          <stop offset="0.8" stop-color="#707070"/>
          <stop offset="1" stop-color="#1a1a1a"/>
        </linearGradient>
      </defs>
      <path d="M0 85 C 110 30, 200 0, 290 6 C 420 14, 520 52, 620 56 C 680 58, 720 57, 750 55 L 750 130 L 0 130 Z" fill="url(#wave-fill)"/>
    </svg>
  </section>

</body>
</html>
```